Need Help Rebranding My Food Blog

I have a Wordpress Food blog called BeetBuddies.com. Right now it has no life and is very bland. I am rebranding this site to a new named called, TheHoneyedPath.com. I would love to have a blog that is vibrant and full of life and personality.

One of my top priorities when a new visitor comes to my site is to quickly understand what the site is about (Gluten-free, dairy-free sweets that taste delicious).

I also want people to feel a connection with me when they come to the site.

Here are some other things that I'd like in the blog design...

1. Optin
My business is driven by adding people to my list so it is very important for me to have an optin front and center/ above-the-fold. See https://www.clevertidyearnings.com/ as an example. The headline that I would like is "Gluten-free & dairy-free sweets that actually taste good"

2. Vibrant/full life
The next important aspect of this blog is that it is vibrant. I like colors that remind me of a SUNSET. See attachments for logo and color scheme. Here's an example of a site I really like that is vibrant: http://www.sugarandopendays.com/

Also see Image titled: "Sample: Feeling". Notice the feeling you get from the image/brush strokes and how it feels light, breezy, and free spirited.

3. Food Images
The last important aspect for my blog is to showcase my recipes. I have attached a few of them as examples. Its really important for a food blog to showcase beautiful pictures of recipes for people to see so will definitely need this in the design.

Also, attached...
1. Image of me.
2. New logo for TheHoneyedPath (notice: don't use the one attached as "Sample/Feeling". That's just for reference of the feeling I like.)

Thanks!

Marion

P.S. I didn't include all the copy that would be needed so feel free to use the "lorem ipsum" text as placeholder if need be.

Target Market(s)

stay-at-home moms, dairy-free & gluten allergies, love desserts & sweets

Coding

Coded - Design and coding required

Font styles to use
Sans Serif

Requirements
Must have
• 1. Optin area with my picture and what I'm about ""Gluten-free & dairy-free sweets that actually taste good""
• 2. Must have personality/vibrancy to the site. Think full of life, not dull like my current website... beetbuddies.com
• 3. Highlight food images (Vertical image holders only)
Nice to have
• Color scheme should be based on my logo
Should not have
• No black or grey colors

```html
<!DOCTYPE html>
<html lang="en">
<head>
<meta charset="utf-8">
<title>TheHoneyedPath — Home</title>
<link href="https://fonts.googleapis.com/css2?family=Philosopher:wght@400;700&family=Open+Sans:wght@400;600&display=swap" rel="stylesheet">
<style>
:root{
  --pink:#e8336e;
  --pink-dark:#d0245c;
  --orange:#f15a24;
  --green:#5b9f1b;
  --green-soft:#d5e6c2;
  --cream:#fdf5ee;
  --panel:#f3f3f3;
  --ink:#3b2e30;
  --ink-soft:#7a6a6c;
  --rule:#eadbd2;
  --white:#ffffff;
  --sunset:linear-gradient(90deg,var(--pink),var(--orange));
}
*{margin:0;padding:0;box-sizing:border-box}
html,body{width:1200px;height:2917px;overflow:hidden;background:var(--white)}
body{font-family:"Open Sans",Arial,sans-serif;color:var(--ink);position:relative}
.heading{font-family:"Philosopher",Georgia,sans-serif;font-weight:400}
.abs{position:absolute}

/* top bar */
.topbar{position:absolute;left:0;top:0;width:1200px;height:31px;background:var(--sunset)}
.topnav{position:absolute;left:156px;top:0;height:31px;display:flex}
.topnav a{color:var(--white);text-decoration:none;font-size:10px;letter-spacing:.5px;line-height:31px;padding:0 17px}
.topnav a.active{background:var(--pink-dark)}
.dropdown{position:absolute;left:298px;top:31px;width:77px;background:var(--pink);padding:4px 0}
.dropdown a{display:block;color:var(--white);font-size:9.5px;letter-spacing:.5px;padding:0 14px;line-height:24px;text-decoration:none}
.social{position:absolute;display:flex;gap:9px}
.social span{width:12px;height:12px;border-radius:50%;background:var(--white);display:block}
.social.top{left:944px;top:10px}
.social.foot{left:549px;top:2857px}
.social.foot span{background:var(--ink)}

.brand{position:absolute;left:0;width:1200px;text-align:center;font-family:"Philosopher",Georgia,sans-serif;font-size:34px;color:var(--pink)}
.brand.head{top:58px}
.brand.foot{top:2660px;color:var(--ink)}

/* hero */
.hero{position:absolute;left:156px;top:152px;width:888px;height:439px;background:linear-gradient(135deg,#5a3020,#8a4a2a 40%,#b8723e 60%,#4a2616)}
.hero-band{position:absolute;left:0;top:158px;width:888px;height:122px;background:rgba(40,18,10,.45)}
.hero-quote{position:absolute;left:0;top:166px;width:888px;text-align:center;color:var(--white);font-size:36px;line-height:48px;letter-spacing:.5px}
.divider{position:absolute;left:156px;width:888px;height:1px;background:#eee}

/* newsletter */
.optin{position:absolute;left:156px;top:640px;width:888px;height:214px;background:var(--panel)}
.optin h2{position:absolute;left:46px;top:42px;font-size:28px;color:var(--ink)}
.optin p{position:absolute;left:46px;top:89px;width:470px;font-size:11.5px;line-height:20px;color:var(--ink-soft)}
.optin .field{position:absolute;left:46px;top:132px;width:310px;height:33px;background:var(--white);border:1px solid #ddd;font-size:10px;color:#bbb;padding:0 14px;line-height:31px}
.optin .send{position:absolute;left:381px;top:132px;width:126px;height:33px;background:var(--sunset);color:var(--white);font-size:11px;font-weight:600;text-align:center;line-height:33px;letter-spacing:.5px}
.optin .photo{position:absolute;left:612px;top:0;width:276px;height:214px;background:radial-gradient(circle at 50% 50%,#8a4a2a 0,#b36a3c 38%,#d9a98a 52%,rgba(243,243,243,0) 68%)}

/* posts */
.posts{position:absolute;left:156px;top:902px;width:560px;height:1654px;border:1px solid #eee}
.post{position:absolute;left:0;width:560px;height:400px}
.post .img{position:absolute;top:0;width:280px;height:400px}
.post .text{position:absolute;top:0;width:280px;height:400px;padding:64px 24px 0}
.post.img-left .img{left:0}.post.img-left .text{left:280px}
.post.img-right .img{left:280px}.post.img-right .text{left:0}
.post h3{font-size:18px;line-height:20px;color:var(--ink)}
.meta{font-size:9.5px;color:var(--ink-soft);margin-top:16px;letter-spacing:.3px}
.cat{font-size:9.5px;color:var(--orange);margin-top:10px;letter-spacing:.5px}
.excerpt{font-size:12px;line-height:20px;color:var(--ink-soft);margin-top:14px;height:82px;overflow:hidden}
.btn{display:inline-block;background:var(--sunset);color:var(--white);font-size:11px;font-weight:600;letter-spacing:.5px;height:34px;line-height:34px;padding:0 16px;margin-top:42px}
.likes{position:absolute;left:214px;top:41px;width:46px;height:46px;border-radius:50%;background:var(--green);color:var(--white);font-size:10px;text-align:center;padding-top:7px;line-height:14px}
.likes svg{display:block;margin:0 auto}
.kale{background:linear-gradient(160deg,#9bb48a,#3f6a2a 40%,#2e4d1f 60%,#c9b79a)}
.cookies{background:linear-gradient(160deg,#f1e8d8,#c99b62 45%,#8b5d35 65%,#e9dcc8)}
.soup{background:linear-gradient(160deg,#f4ede3,#f0d9a0 45%,#e6c178 60%,#f3ece4)}
.donuts{background:linear-gradient(160deg,#6b3a22,#3e2014 40%,#d8c7b8 70%,#4a2818)}
.pager{position:absolute;left:0;top:1599px;width:558px;height:54px;display:flex}
.pager span{flex:1;text-align:center;line-height:54px;font-size:11px;letter-spacing:.5px;color:var(--white)}
.pager .prev{background:var(--green-soft);color:#8aa87a}
.pager .next{background:var(--green)}

/* sidebar */
.sidebar{position:absolute;left:764px;top:902px;width:280px;height:1654px;background:var(--cream)}
.sidebar h4{position:absolute;left:0;width:280px;text-align:center;font-size:18px;color:var(--ink)}
.avatar{position:absolute;left:52px;top:106px;width:176px;height:176px;border-radius:50%;background:linear-gradient(160deg,#7aa86a,#3f6a3a 55%,#2d4a2a)}
.bio{position:absolute;left:28px;top:297px;width:224px;text-align:center;font-size:11px;line-height:20px;color:var(--ink-soft)}
.sidebar .btn{position:absolute;left:76px;top:407px;margin:0;width:128px;text-align:center;padding:0}
.rule{position:absolute;left:24px;width:232px;height:1px;background:var(--rule)}
.mini{position:absolute;left:24px;width:240px;height:70px}
.mini .thumb{position:absolute;left:0;top:0;width:70px;height:70px;border-radius:50%}
.mini .t{position:absolute;left:86px;top:8px;width:150px;font-family:"Philosopher",Georgia,sans-serif;font-size:15px;line-height:19px;color:var(--ink)}
.mini .c{position:absolute;left:86px;width:150px;font-size:9px;color:var(--orange)}
.popcorn{background:radial-gradient(circle,#f0dcc0,#c57a4a)}
.broccoli{background:radial-gradient(circle,#e8c27a,#c99050)}
.mac{background:radial-gradient(circle,#f2b24a,#6a3a1e)}
.bark{background:radial-gradient(circle,#c85a3a,#3a2016)}
.potato{background:radial-gradient(circle,#f3e3b4,#efe9e0)}
.ad{position:absolute;left:24px;top:1267px;width:231px;height:324px;background:linear-gradient(180deg,#fff 0,#fff 28%,#e8b860 45%,#d9c88a 62%,#7fb04a 75%,#d09a5a 88%)}

/* footer */
.footer{position:absolute;left:0;top:2606px;width:1200px;height:311px;background:linear-gradient(180deg,#fdd0e6,#fdd2c2)}
.foot-rule{position:absolute;left:156px;top:2758px;width:888px;height:1px;background:#e9a9b6}
.up{position:absolute;left:583px;top:2741px;width:34px;height:34px;border-radius:50%;background:var(--orange)}
.footnav{position:absolute;left:0;top:2792px;width:1200px;display:flex;justify-content:center;gap:36px;font-size:10.5px;letter-spacing:.5px}
.footnav a{color:var(--ink);text-decoration:none}
.footnav a.active{color:var(--orange)}
.copy{position:absolute;left:0;top:2826px;width:1200px;text-align:center;font-size:10px;color:var(--ink)}
</style>
</head>
<body>

<header class="topbar">
  <nav class="topnav">
    <a href="#">HOME</a><a href="#">ABOUT</a><a href="#" class="active">RECIPES</a><a href="#">RESOURCES</a>
  </nav>
  <div class="social top"><span></span><span></span><span></span><span></span><span></span><span></span></div>
</header>
<div class="dropdown"><a href="#">COOKIES</a><a href="#">CAKES</a><a href="#">DONETS</a><a href="#">SWEETS</a></div>

<div class="brand head">TheHoneyedPath</div>

<section class="hero" role="img" aria-label="Chocolate glazed donuts with rainbow sprinkles on a cooling rack">
  <div class="hero-band"></div>
  <p class="hero-quote heading">“Gluten-free &amp; dairy-free sweets<br>that actually taste good”</p>
</section>

<div class="divider" style="top:617px"></div>

<section class="optin">
  <h2 class="heading">Subscribe Our Newsletter</h2>
  <p>Enter your email address to subscribe to this blog and receive notifications of new posts by email.</p>
  <div class="field">Enter Your Email Address</div>
  <div class="send">SEND &#10148;</div>
  <div class="photo" role="img" aria-label="Stack of chocolate glazed donuts"></div>
</section>

<main class="posts">
  <article class="post img-left" style="top:0">
    <div class="img kale" role="img" aria-label="Bowl of sauteed kale with lemon slices"></div>
    <div class="likes"><svg width="12" height="11" viewBox="0 0 12 11"><path d="M6 10 1.5 5.5A2.6 2.6 0 0 1 6 2a2.6 2.6 0 0 1 4.5 3.5Z" fill="none" stroke="#fff" stroke-width="1.2"/></svg>60</div>
    <div class="text">
      <h3 class="heading">Sauteed Kale with Lemon and Ginger</h3>
      <div class="meta">&#9638; AUGUST 3, 2015 &nbsp;&nbsp; &#9675; 3 COMMENTS</div>
      <div class="cat">DINNER, LUNCH, VEGAN</div>
      <p class="excerpt">We have been home for five days. I am so happy to be sleeping in my own bed. Today was the first day, I felt like I wasn't on vacation any more. My son, Rowan, has been [...]</p>
      <span class="btn">LEARN MORE &#10148;</span>
    </div>
  </article>

  <article class="post img-right" style="top:400px">
    <div class="img cookies" role="img" aria-label="Blueberry chocolate chip oatmeal bites on parchment"></div>
    <div class="likes" style="left:494px"><svg width="12" height="11" viewBox="0 0 12 11"><path d="M6 10 1.5 5.5A2.6 2.6 0 0 1 6 2a2.6 2.6 0 0 1 4.5 3.5Z" fill="none" stroke="#fff" stroke-width="1.2"/></svg>120</div>
    <div class="text">
      <h3 class="heading">Blueberry Chocolate Chip Oatmeal Minis</h3>
      <div class="meta">&#9638; AUGUST 12, 2016 &nbsp;&nbsp; &#9675; 23 COMMENTS</div>
      <div class="cat">DESSERT</div>
      <p class="excerpt">I just LOVE Blueberries. It turns out that my little cutie loves them as much as I do! Last summer was the first time I went fruit picking with Clara without my hubby. She was [...]</p>
      <span class="btn">LEARN MORE &#10148;</span>
    </div>
  </article>

  <article class="post img-left" style="top:800px">
    <div class="img soup" role="img" aria-label="Bowl of creamy potato soup topped with bacon and scallions"></div>
    <div class="likes"><svg width="12" height="11" viewBox="0 0 12 11"><path d="M6 10 1.5 5.5A2.6 2.6 0 0 1 6 2a2.6 2.6 0 0 1 4.5 3.5Z" fill="none" stroke="#fff" stroke-width="1.2"/></svg>19</div>
    <div class="text">
      <h3 class="heading">Dairy-Free Creamy Potato Soup</h3>
      <div class="meta">&#9638; AUGUST 25, 2016 &nbsp;&nbsp; &#9675; 23 COMMENTS</div>
      <div class="cat">DINNER, LUNCH</div>
      <p class="excerpt">It's another rainy day here in San Jose. Dark clouds and chilly air leave me curled up on the couch with both a sweater and blanket. as we left church, that it actually broke [...]</p>
      <span class="btn">LEARN MORE &#10148;</span>
    </div>
  </article>

  <article class="post img-right" style="top:1197px">
    <div class="img donuts" role="img" aria-label="Chocolate and coconut glazed donuts with sprinkles"></div>
    <div class="likes" style="left:494px"><svg width="12" height="11" viewBox="0 0 12 11"><path d="M6 10 1.5 5.5A2.6 2.6 0 0 1 6 2a2.6 2.6 0 0 1 4.5 3.5Z" fill="none" stroke="#fff" stroke-width="1.2"/></svg>26</div>
    <div class="text">
      <h3 class="heading">Blueberry Chocolate Chip Oatmeal Minis</h3>
      <div class="meta">&#9638; AUGUST 19, 2016 &nbsp;&nbsp; &#9675; 22 COMMENTS</div>
      <div class="cat">DESSERT</div>
      <p class="excerpt">It's the most wonderful time of year. The Christmas season always puts me in baking mode. The heat from the oven makes the house warm and toasty and I love smelling baked [...]</p>
      <span class="btn">LEARN MORE &#10148;</span>
    </div>
  </article>

  <div class="pager"><span class="prev">&#10094; PREV POSTS</span><span class="next">NEXT POSTS &#10148;</span></div>
</main>

<aside class="sidebar">
  <h4 class="heading" style="top:55px">Meet Me</h4>
  <div class="avatar" role="img" aria-label="Portrait of the blog author and her husband"></div>
  <p class="bio">Welcome to BeetBuddies. My name is Marion and my husband's name is Grant. We have two beet buddies: Clara and Rowan. Between my husband and I we have 7 allergies.</p>
  <span class="btn">VIEW MORE &#10148;</span>
  <div class="rule" style="top:491px"></div>

  <h4 class="heading" style="top:533px">Recent Posts</h4>
  <div class="mini" style="top:577px"><div class="thumb popcorn" role="img" aria-label="Cinnamon swirl popcorn"></div><div class="t">Cinnamon Swirl Popcorn</div><div class="c" style="top:50px">&#9675; 4 COMMENTS</div></div>
  <div class="mini" style="top:682px"><div class="thumb broccoli" role="img" aria-label="Cream of broccoli soup"></div><div class="t">Cream of Broccoli Soup (Dairy-free)</div><div class="c" style="top:50px">&#9675; 18 COMMENTS</div></div>
  <div class="rule" style="top:802px"></div>

  <h4 class="heading" style="top:844px">Most Popular</h4>
  <div class="mini" style="top:891px"><div class="thumb mac" role="img" aria-label="Gluten-free mac n cheese"></div><div class="t">Gluten-free Mac n Cheese</div><div class="c" style="top:50px">&#9675; 4 COMMENTS</div></div>
  <div class="mini" style="top:994px"><div class="thumb bark" role="img" aria-label="Pretzel peppermint chocolate bark"></div><div class="t">Pretzel Peppermint Chocolate Bark</div><div class="c" style="top:50px">&#9675; 18 COMMENTS</div></div>
  <div class="mini" style="top:1095px"><div class="thumb potato" role="img" aria-label="Dairy-free creamy potato soup"></div><div class="t">Dairy-Free Creamy Potato Soup</div><div class="c" style="top:50px">&#9675; 18 COMMENTS</div></div>
  <div class="rule" style="top:1218px"></div>

  <div class="ad" role="img" aria-label="Promotional graphic for a vegan chickpea salad sandwich"></div>
</aside>

<footer class="footer"></footer>
<div class="brand foot">TheHoneyedPath</div>
<div class="foot-rule"></div>
<div class="up"><svg width="34" height="34" viewBox="0 0 34 34"><path d="M11 20 17 14 23 20" fill="none" stroke="#fff" stroke-width="2.4"/></svg></div>
<nav class="footnav"><a href="#" class="active">HOME</a><a href="#">ABOUT</a><a href="#">RECIPES</a><a href="#">RESOURCES</a></nav>
<p class="copy">TheHoneyedPath © 2017. All rights reserved. Terms of use and Privacy Policy</p>
<div class="social foot"><span></span><span></span><span></span><span></span><span></span></div>

</body>
</html>
```